Real Estate Investing company needs a business card design

We need a business card design for new Real Estate Investment Company called "Maple Ridge Ventures, LLC." We buy homes for cash and close quickly in any situation. Our company provides an easy and fast option for home owners who are in tough situations who need to sell their home fast and don't want realtor fees or other listing hassles. We also renovate and resell our homes which helps provide housing for the community. We would like to see designs that use the colors blue and white to match our company logo or other colors that may match our company logo. The final design should communicate trust and easy process.
Industry/Entity Type
Business
Contact Information for Business Card
Front should have company name and company logo. back of card should have company logo and area to list services.
Look and feel

```html
<!DOCTYPE html>
<html lang="en">
<head>
<meta charset="utf-8">
<title>Maple Ridge Ventures – Business Card</title>
<link href="https://fonts.googleapis.com/css2?family=Open+Sans:wght@400;600;700&display=swap" rel="stylesheet">
<style>
  :root {
    --brand-blue: #1565b8;
    --soft-grey: #c7c8ca;
    --text-grey: #8a8c8f;
    --card-white: #ffffff;
    --card-dark: #262626;
    --backdrop: #e9e7e4;
  }
  * { margin: 0; padding: 0; box-sizing: border-box; }
  html, body { width: 1200px; height: 1000px; overflow: hidden; }
  body {
    position: relative;
    background: var(--backdrop);
    font-family: "Open Sans", Arial, sans-serif;
  }
  .card {
    position: absolute;
    left: 265px;
    width: 665px;
    height: 397px;
    overflow: hidden;
    box-shadow: 0 6px 18px rgba(0,0,0,0.18);
  }
  .card--front { top: 73px; background: var(--card-white); }
  .card--back  { top: 532px; background: var(--card-dark); }

  .wordmark {
    position: absolute;
    display: flex;
    align-items: center;
    gap: 14px;
    color: var(--brand-blue);
    font-weight: 700;
    text-transform: uppercase;
    line-height: 1.02;
  }
  .wordmark__square {
    width: 22px; height: 22px;
    background: var(--brand-blue);
    flex: none;
  }
  .card--front .wordmark { left: 33px; top: 45px; font-size: 40px; }
  .card--back .wordmark {
    left: 0; right: 0; top: 140px;
    justify-content: center;
    font-size: 50px;
    text-align: left;
  }
  .card--back .wordmark__square { width: 28px; height: 28px; }

  .holder { position: absolute; left: 32px; top: 202px; }
  .holder__name { color: var(--brand-blue); font-weight: 700; font-size: 22px; letter-spacing: 0.3px; }
  .holder__title { color: var(--text-grey); font-size: 16px; margin-top: 2px; }

  .contact { position: absolute; left: 33px; top: 274px; list-style: none; }
  .contact li {
    display: flex; align-items: center; gap: 10px;
    color: var(--text-grey); font-size: 16px; height: 24.5px;
  }
  .contact svg { width: 14px; height: 14px; fill: var(--brand-blue); flex: none; }

  .services { position: absolute; left: 408px; top: 174px; }
  .services__heading { color: var(--brand-blue); font-weight: 700; font-size: 19px; margin-bottom: 4px; }
  .services__list { list-style: none; }
  .services__list li {
    display: flex; align-items: center; gap: 8px;
    color: var(--text-grey); font-size: 15.5px; height: 22px;
  }
  .services__list svg { width: 14px; height: 12px; flex: none; }

  .swoosh { position: absolute; left: 0; bottom: 0; width: 665px; height: 397px; }
  .website {
    position: absolute; right: 32px; bottom: 8px;
    color: var(--brand-blue); font-size: 16px;
  }
</style>
</head>
<body>

<section class="card card--front" aria-label="Business card front">
  <div class="wordmark"><span class="wordmark__square"></span><span>Maple Ridge<br>Ventures</span></div>

  <div class="holder">
    <p class="holder__name">DANIEL REYES</p>
    <p class="holder__title">Chief Executive Officer</p>
  </div>

  <ul class="contact">
    <li><svg viewBox="0 0 14 14"><rect x="4" y="0" width="6" height="14" rx="1"/></svg>+ 000 000 0000</li>
    <li><svg viewBox="0 0 14 14"><rect x="3" y="0" width="8" height="4"/><rect x="0" y="4" width="14" height="6" rx="1"/><rect x="3" y="9" width="8" height="5"/></svg>+ 000 000 0000</li>
    <li><svg viewBox="0 0 14 14"><path d="M0 3h14v8H0z M0 3l7 5 7-5" stroke="#fff" stroke-width="1"/></svg>info@mapleridgeventures.com</li>
  </ul>

  <div class="services">
    <p class="services__heading">SERVICES</p>
    <ul class="services__list">
      <li><svg viewBox="0 0 14 12"><path d="M1 6l4 4 8-9" fill="none" stroke="#1565b8" stroke-width="2"/></svg>Lead Generation</li>
      <li><svg viewBox="0 0 14 12"><path d="M1 6l4 4 8-9" fill="none" stroke="#1565b8" stroke-width="2"/></svg>Customer Acquisition</li>
      <li><svg viewBox="0 0 14 12"><path d="M1 6l4 4 8-9" fill="none" stroke="#1565b8" stroke-width="2"/></svg>Internet Marketing</li>
      <li><svg viewBox="0 0 14 12"><path d="M1 6l4 4 8-9" fill="none" stroke="#1565b8" stroke-width="2"/></svg>Phone Verified Leads</li>
      <li><svg viewBox="0 0 14 12"><path d="M1 6l4 4 8-9" fill="none" stroke="#1565b8" stroke-width="2"/></svg>Performance Analytics</li>
      <li><svg viewBox="0 0 14 12"><path d="M1 6l4 4 8-9" fill="none" stroke="#1565b8" stroke-width="2"/></svg>Inbound Services</li>
    </ul>
  </div>

  <svg class="swoosh" viewBox="0 0 665 397" aria-hidden="true">
    <path d="M200 397 C360 372 520 362 665 360 L665 397 Z" fill="var(--soft-grey)"/>
    <path d="M0 386 C150 366 330 358 480 358 C330 363 150 378 0 397 Z" fill="var(--brand-blue)"/>
  </svg>
  <p class="website">www.mapleridgeventures.com</p>
</section>

<section class="card card--back" aria-label="Business card back">
  <div class="wordmark"><span class="wordmark__square"></span><span>Maple Ridge<br>Ventures</span></div>
</section>

</body>
</html>
```